External Window Signage Design – Antiaging Center

I would like to dress our shop windows in order to promote our activities in medical aesthetics, meso-aesthetics, anti-ageing care and classical beauty. In fact, our 350 m² center is located on the first floor of a building where there is a lot of traffic, as well as a bus stop and metro station. And right in front of a twenty-floor building of the Northern Assembly.
We want to communicate our activities to our customers with photos and text in a storefront window. So that they can what we do and visit our website www.lumivora.be (our site is in French) as well as our social networks, like instragram, facebook,…
We'd like a window signage : Elegant, Modern, New, Pure, Clean
We are located on the corners of a building, where we have 8 windows on one side and 10 windows on the other, the dimensions are :
Windows
• Height: 125 cm
• Width: 130 cm
Small windows
• Height: 134 cm
• Width: 40 cm
I would say let your imagination go free. I will have other projects for the winner.
Don't hesitate to ask me if you need other formats of the logo or color, like white.
Updates

https://www.brieflyhub.com/design/58204719, I'D LIKE TO HAVE A PROJECT LIKE THIS IF POSSIBLE WITH THE LITTLE WINDOW UNDERNEATH AS WELL.

Target Market(s)

People who want to take care of their external appearance, look beautiful and good looking, womens/girls - mens/boys

Requirements
Must have
• Face and silhouette of a woman. Elegant
Serious, Modern, Professional, Feminine,Upmarket
Nice to have
• To put the different treatments that we propose,
Should not have
• We absolutely don't want a classic beauty center signage, which is reviewed many times

```html
<!DOCTYPE html>
<html lang="en">
<head>
<meta charset="utf-8">
<title>Lumivora Antiaging Center – Window Signage</title>
<link href="https://fonts.googleapis.com/css2?family=Heebo:wght@300;400;700&family=Open+Sans:wght@400&display=swap" rel="stylesheet">
<style>
  :root{
    --red:#c8102e;
    --band-red:#d42a55;
    --gold:#b0935a;
    --gold-band:#c2a86c;
    --ink:#3a3a3a;
    --label:#555555;
    --stage-light:#ececec;
    --stage-dark:#b9b9b9;
  }
  *{margin:0;padding:0;box-sizing:border-box}
  html,body{width:1200px;height:1200px;overflow:hidden}
  body{
    position:relative;
    background:linear-gradient(90deg,var(--stage-dark) 0%,var(--stage-light) 45%,var(--stage-light) 55%,var(--stage-dark) 100%);
    font-family:"Heebo",Arial,sans-serif;
  }
  .panel{position:absolute;top:222px;height:757px;background:#fff;overflow:hidden}
  .panel--small{left:68px;width:225px;background:linear-gradient(180deg,#f1f1f1 0%,#fff 18%,#fff 100%)}
  .panel--window{left:339px;width:787px}
  .panel svg.layer{position:absolute;left:0;top:0}
  .size-label{position:absolute;top:992px;font-family:"Heebo",Arial,sans-serif;font-weight:300;font-size:30px;color:#222;text-align:center}
  .size-label--small{left:68px;width:225px}
  .size-label--window{left:339px;width:787px}
  .wordmark{font-family:"Heebo",Arial,sans-serif;font-weight:700;fill:var(--ink);letter-spacing:-1px}
  .subtitle{font-family:"Open Sans",Arial,sans-serif;font-weight:400;fill:var(--ink)}
  .headline{font-family:"Heebo",Arial,sans-serif;font-weight:300;fill:var(--red)}
  .treatment{font-family:"Heebo",Arial,sans-serif;font-weight:300;fill:var(--gold)}
  .fact{font-family:"Heebo",Arial,sans-serif;font-weight:400;fill:var(--label)}
  .web{font-family:"Heebo",Arial,sans-serif;font-weight:300}
</style>
</head>
<body>

<svg width="0" height="0" style="position:absolute">
  <defs>
    <symbol id="icon-sessions" viewBox="0 0 40 40">
      <g fill="#c8102e">
        <text x="0" y="11" font-family="Heebo,Arial,sans-serif" font-weight="700" font-size="12">1</text>
        <text x="0" y="25" font-family="Heebo,Arial,sans-serif" font-weight="700" font-size="12">2</text>
        <text x="0" y="39" font-family="Heebo,Arial,sans-serif" font-weight="700" font-size="12">3</text>
        <rect x="11" y="5" width="28" height="5"/>
        <rect x="11" y="18" width="28" height="5"/>
        <rect x="11" y="31" width="28" height="5"/>
      </g>
    </symbol>
    <symbol id="icon-timer" viewBox="0 0 40 40">
      <g fill="none" stroke="#c8102e" stroke-width="1.6" stroke-linecap="round">
        <circle cx="22" cy="22" r="14" stroke-dasharray="3 2"/>
        <line x1="22" y1="22" x2="28" y2="14"/>
        <line x1="19" y1="4" x2="25" y2="4"/>
        <line x1="22" y1="4" x2="22" y2="8"/>
        <line x1="2" y1="18" x2="8" y2="18"/>
        <line x1="0" y1="23" x2="7" y2="23"/>
        <line x1="3" y1="28" x2="9" y2="28"/>
      </g>
    </symbol>
    <symbol id="icon-price" viewBox="0 0 40 40">
      <path d="M4 24 L22 6 L36 4 L34 18 L16 36 Z" fill="#c8102e"/>
      <circle cx="29" cy="11" r="3" fill="#fff"/>
    </symbol>
    <symbol id="icon-repeat" viewBox="0 0 40 40">
      <g fill="none" stroke="#c8102e" stroke-width="2.4" stroke-linecap="round">
        <path d="M9 12 A15 15 0 1 1 6 22"/>
        <polyline points="3,8 9,13 14,6"/>
      </g>
    </symbol>
    <linearGradient id="portrait-tone" x1="0" y1="0" x2="1" y2="0">
      <stop offset="0" stop-color="#ecc9b6"/>
      <stop offset="0.6" stop-color="#f5e0d5"/>
      <stop offset="1" stop-color="#ffffff" stop-opacity="0"/>
    </linearGradient>
    <linearGradient id="portrait-tone-v" x1="0" y1="0" x2="0" y2="1">
      <stop offset="0" stop-color="#a88768" stop-opacity="0.55"/>
      <stop offset="0.25" stop-color="#f3dccf" stop-opacity="0"/>
    </linearGradient>
  </defs>
</svg>

<!-- Small window: 134 x 40 cm -->
<section class="panel panel--small">
  <svg class="layer" width="225" height="757" viewBox="0 0 225 757">
    <g role="img" aria-label="Portrait photo of a serene young woman with eyes closed, hands framing her face">
      <rect x="0" y="300" width="225" height="400" fill="url(#portrait-tone)"/>
      <rect x="0" y="300" width="225" height="400" fill="url(#portrait-tone-v)"/>
    </g>

    <g class="brand">
      <circle cx="33" cy="56" r="19" fill="var(--gold)"/>
      <text class="wordmark" x="209" y="63" font-size="36" text-anchor="end">Lumivora</text>
      <text class="subtitle" x="187" y="78" font-size="10.5" text-anchor="end">Antiaging Center</text>
    </g>
    <text class="headline" x="112" y="152" font-size="36" text-anchor="middle" letter-spacing="-1">ANTIAGING</text>
    <line x1="65" y1="158" x2="161" y2="158" stroke="var(--ink)" stroke-width="1"/>
    <text class="treatment" x="112" y="183" font-size="23.5" text-anchor="middle">Wrinkle Filling</text>

    <g class="facts">
      <use href="#icon-sessions" x="26" y="215" width="24" height="24"/>
      <use href="#icon-timer" x="77" y="215" width="24" height="24"/>
      <use href="#icon-price" x="128" y="215" width="24" height="24"/>
      <use href="#icon-repeat" x="176" y="215" width="24" height="24"/>
      <g stroke="#cfcfcf" stroke-width="0.8">
        <line x1="60" y1="216" x2="60" y2="250"/>
        <line x1="117" y1="216" x2="117" y2="250"/>
        <line x1="168" y1="216" x2="168" y2="250"/>
      </g>
      <text class="fact" x="38" y="250" font-size="7" text-anchor="middle">1 session</text>
      <text class="fact" x="89" y="250" font-size="7" text-anchor="middle">+/- 45minutes</text>
      <text class="fact" x="140" y="250" font-size="7" text-anchor="middle">From 180 €</text>
      <text class="fact" x="188" y="246" font-size="7" text-anchor="middle">9 to 12</text>
      <text class="fact" x="188" y="253" font-size="7" text-anchor="middle">months</text>
    </g>

    <g class="bands">
      <polygon points="0,583 53,612 0,638" fill="var(--gold-band)"/>
      <polygon points="0,632 225,556 225,562 0,638" fill="#ffffff"/>
      <polygon points="0,638 225,562 225,618 0,696" fill="var(--band-red)" fill-opacity="0.92"/>
      <polygon points="81,671 225,618 225,716" fill="var(--gold-band)"/>
    </g>

    <text class="web" x="112" y="717" font-size="13" text-anchor="middle" fill="var(--red)">www.lumivora.be</text>
    <circle cx="99" cy="736" r="6" fill="#5a5a5a"/>
    <circle cx="118" cy="736" r="6" fill="#5a5a5a"/>
  </svg>
</section>
<div class="size-label size-label--small">134 cm x 40 cm</div>

<!-- Window: 125 x 130 cm -->
<section class="panel panel--window">
  <svg class="layer" width="787" height="757" viewBox="0 0 787 757">
    <g role="img" aria-label="Large portrait photo of a serene young woman with eyes closed, hands gently framing her face">
      <rect x="0" y="0" width="500" height="757" fill="url(#portrait-tone)"/>
      <rect x="0" y="0" width="500" height="757" fill="url(#portrait-tone-v)"/>
    </g>

    <g class="brand">
      <circle cx="402" cy="90" r="44" fill="var(--gold)"/>
      <text class="wordmark" x="745" y="104" font-size="71" text-anchor="end">Lumivora</text>
      <text class="subtitle" x="698" y="128" font-size="22" text-anchor="end">Antiaging Center</text>
    </g>

    <text class="headline" x="745" y="269" font-size="70" text-anchor="end" letter-spacing="-1">Antiaging</text>
    <text class="treatment" x="745" y="325" font-size="40" text-anchor="end">Wrinkle Filling</text>

    <g class="facts">
      <use href="#icon-sessions" x="474" y="387" width="38" height="38"/>
      <use href="#icon-timer" x="550" y="387" width="38" height="38"/>
      <use href="#icon-price" x="629" y="387" width="38" height="38"/>
      <use href="#icon-repeat" x="702" y="387" width="38" height="38"/>
      <g stroke="#cfcfcf" stroke-width="1">
        <line x1="526" y1="390" x2="526" y2="440"/>
        <line x1="611" y1="390" x2="611" y2="440"/>
        <line x1="689" y1="390" x2="689" y2="440"/>
      </g>
      <text class="fact" x="492" y="443" font-size="10.5" text-anchor="middle">1 session</text>
      <text class="fact" x="569" y="443" font-size="10.5" text-anchor="middle">+/- 45minutes</text>
      <text class="fact" x="648" y="443" font-size="10.5" text-anchor="middle">From 180 €</text>
      <text class="fact" x="721" y="443" font-size="10.5" text-anchor="middle">9 to 12</text>
      <text class="fact" x="721" y="453" font-size="10.5" text-anchor="middle">months</text>
    </g>

    <g class="bands">
      <polygon points="0,604 189,697 0,757" fill="var(--gold-band)" fill-opacity="0.95"/>
      <polygon points="30,757 470,606 476,620 89,757" fill="#ffffff"/>
      <polygon points="89,757 476,620 787,509 787,700 627,757" fill="var(--band-red)" fill-opacity="0.9"/>
      <polygon points="627,757 787,700 787,757" fill="var(--gold-band)"/>
    </g>

    <text class="web" x="745" y="641" font-size="26" text-anchor="end" fill="#ffffff">www.lumivora.be</text>
    <circle cx="695" cy="673" r="12" fill="#ffffff"/>
    <circle cx="732" cy="673" r="12" fill="#ffffff"/>
  </svg>
</section>
<div class="size-label size-label--window">125 cm x 130 cm</div>

</body>
</html>
```